Business Cards for cafe providing speciality coffee and food

I need a business card design for my husband’s businesses. He has two cafes in Brisbane. The business name is Copperleaf Roasting House. They sell high end specialty coffee as well as breakfast and lunch. All the food is cooked fresh, in house and they have strict quality controls for their coffee. I would like the business card to feature the address for both cafes, my husband’s phone number and the business’s instagram. The address for the first is 61 Walden Crescent, Oakvale and the second is 23 Pellow Avenue, Brindlemoor. The Instagram handle is @copperleafroastinghouse and phone number is 0491362847. We already have a business logo that is attached.

Target Market(s)

All ages, higher disposable income and more likely to eat out regularly

Industry/Entity Type

Hospitality

Contact Information for Business Card

Must be suitable for both customers and suppliers

Font styles to use
Sans Serif

Colors

Designer to choose colors to be used in the design.

Requirements
Must have
• Owner’s name: Reid Castell
• Addresses of both cafes: 61 Walden Crescent, Oakvale and 23 Pellow Avenue, Brindlemoor
• Instagram handle: @copperleafroastinghouse
• Contact number: 0491362847
Nice to have
• Business logo

```html
<!DOCTYPE html>
<html lang="en">
<head>
<meta charset="utf-8">
<title>Copperleaf Roasting House – Business Card</title>
<link rel="stylesheet" href="https://fonts.googleapis.com/css2?family=Open+Sans:wght@400;700&display=swap">
<style>
  :root {
    --backdrop: #2a2a2a;
    --card-dark: #0b0b0b;
    --card-light: #ffffff;
    --ink-dark: #111111;
    --ink-light: #ffffff;
    --rule: #1a1a1a;
  }
  * { margin: 0; padding: 0; box-sizing: border-box; }
  html, body {
    width: 1200px;
    height: 900px;
    overflow: hidden;
    background: var(--backdrop);
    font-family: "Open Sans", Arial, sans-serif;
  }
  .stage {
    position: relative;
    width: 1200px;
    height: 900px;
  }
  .card {
    position: absolute;
    left: 290px;
    width: 620px;
    height: 354px;
    box-shadow: 0 10px 28px rgba(0,0,0,0.45);
  }
  .card--front {
    top: 62px;
    background: var(--card-dark);
    display: flex;
    align-items: center;
    justify-content: center;
  }
  .card--back {
    top: 478px;
    background: var(--card-light);
    color: var(--ink-dark);
    display: flex;
    align-items: center;
  }

  /* Brand mark: name set in text with one plain circle */
  .brand {
    display: flex;
    flex-direction: column;
    align-items: center;
    gap: 12px;
    text-align: center;
  }
  .brand__circle {
    width: 64px;
    height: 64px;
    border-radius: 50%;
    border: 3px solid currentColor;
  }
  .brand__name {
    font-weight: 700;
    font-size: 20px;
    line-height: 1.2;
    letter-spacing: 0.06em;
    text-transform: uppercase;
    max-width: 220px;
  }
  .card--front .brand { color: var(--ink-light); }
  .card--back .brand { color: var(--ink-dark); }

  .back__brand-col {
    width: 262px;
    display: flex;
    justify-content: center;
    padding-left: 20px;
  }
  .back__divider {
    width: 2px;
    height: 150px;
    background: var(--rule);
  }
  .back__details {
    padding-left: 30px;
  }
  .owner {
    font-weight: 700;
    font-size: 21px;
    letter-spacing: 0.01em;
    text-transform: uppercase;
    margin-bottom: 10px;
    padding-left: 20px;
  }
  .contact-line {
    display: flex;
    align-items: center;
    gap: 9px;
    font-size: 15px;
    line-height: 1.45;
  }
  .contact-line svg { width: 14px; height: 14px; flex: none; }
  .addresses {
    margin-top: 8px;
    font-size: 15px;
    line-height: 1.3;
  }
</style>
</head>
<body>
<main class="stage">

  <section class="card card--front" aria-label="Business card front">
    <div class="brand">
      <span class="brand__circle" aria-hidden="true"></span>
      <span class="brand__name">Copperleaf Roasting House</span>
    </div>
  </section>

  <section class="card card--back" aria-label="Business card back">
    <div class="back__brand-col">
      <div class="brand">
        <span class="brand__circle" aria-hidden="true"></span>
        <span class="brand__name">Copperleaf Roasting House</span>
      </div>
    </div>
    <div class="back__divider" aria-hidden="true"></div>
    <div class="back__details">
      <h1 class="owner">Reid Castell</h1>
      <p class="contact-line">
        <svg viewBox="0 0 24 24" aria-hidden="true"><path fill="currentColor" d="M6.6 10.8a15.1 15.1 0 0 0 6.6 6.6l2.2-2.2a1 1 0 0 1 1-.25 11.4 11.4 0 0 0 3.6.57 1 1 0 0 1 1 1V20a1 1 0 0 1-1 1A17 17 0 0 1 3 4a1 1 0 0 1 1-1h3.5a1 1 0 0 1 1 1c0 1.25.2 2.45.57 3.57a1 1 0 0 1-.25 1z"/></svg>
        <span>0491362847</span>
      </p>
      <p class="contact-line">
        <svg viewBox="0 0 24 24" aria-hidden="true"><rect x="3" y="3" width="18" height="18" fill="none" stroke="currentColor" stroke-width="2.4"/></svg>
        <span>@copperleafroastinghouse</span>
      </p>
      <p class="addresses">
        61 Walden Crescent<br>
        Oakvale and 23 Pellow Avenue<br>
        Brindlemoor
      </p>
    </div>
  </section>

</main>
</body>
</html>
```